Web Site Design for a Finance (lending) Company

We are opening a new subsidiary that focuses on lending money in the real estate industry. We need a web site designed to represent the business.

The business is lending money to real estate investors. A typical client/borrower will be looking to borrow money to buy a house, renovate it and then sell it at a profit, all within 12 months or less.

Company name is Brevand Finance. Our logo is attached.

Attached is a general outline for the web site. We're working on writing more text for each page but this should give you enough to get started with some ideas.

Competitor web site that I like a lot (as an example): https://quorvelfunding.com/. Many of the general items on this site match what we will need (description of loan programs, FAQ)

Target Market(s)

Real estate investors (generally individuals or small companies with just a few people) who are buying homes, renovating them and then selling them at a profit.

Industry/Entity Type

Finance

Coding

Coded - Design and coding required

Number of Pages Required

5+ page

Colors

Designer to choose colors to be used in the design.

Requirements
Must have
• Minimalist design. Clean lines without too much clutter. Some stock photography is ok but the photos should not be distracting. They should almost fade in to the background so that user can focus on the key information about what our company does instead. We are a finance company, not a design company, so the information about our products will be more interesting to site visitors than the art.
• Some minimalist examples from Snapboard:
• https://www.snapboard-example.com/explore/minimalist-web-design/
Nice to have
• If you search in seekly for "hard money lenders" you will find many examples of web sites from our competition. I have provided a link above to competitor web site that I like a lot.
• I have attached our logo in EPS format. Logo is green. Web site doesn't have to be green but it should be of a color that will work well with the logo.

```html
<!DOCTYPE html>
<html lang="en">
<head>
<meta charset="utf-8">
<title>Brevand Finance</title>
<link rel="stylesheet" href="https://fonts.googleapis.com/css2?family=Roboto:wght@300;400;500;700&display=swap">
<style>
:root{
  --green:#0d6332;
  --green-dark:#0a5229;
  --green-band:#0f6b36;
  --ink:#333;
  --muted:#666;
  --line:#e2e2e2;
  --soft:#f3f3f3;
  --white:#fff;
}
*{box-sizing:border-box;margin:0;padding:0}
html,body{width:1200px;height:2534px;overflow:hidden;background:var(--white)}
body{font-family:'Roboto',Arial,sans-serif;color:var(--ink);position:relative}
.abs{position:absolute}
.btn{position:absolute;background:var(--green);color:var(--white);font-size:10px;display:flex;align-items:center;justify-content:center;gap:6px;border-radius:2px}
.btn .chev{font-size:11px}

/* header */
.site-header{position:absolute;left:0;top:0;width:1200px;height:60px;border-bottom:1px solid var(--line);background:var(--white)}
.brand{position:absolute;display:flex;align-items:center;gap:8px;color:var(--green);font-weight:500}
.brand .mark{width:14px;height:14px;background:var(--green)}
.main-nav{position:absolute;left:395px;top:24px;display:flex;gap:24px;font-size:10px;color:#333}
.main-nav .active{border-bottom:1px solid var(--green);padding-bottom:3px}
.social{position:absolute;display:flex;gap:6px}
.social span{width:9px;height:9px;border-radius:50%;background:#555}
.login{position:absolute;left:818px;top:24px;font-size:10px}
.divider-v{position:absolute;left:806px;top:20px;width:1px;height:18px;background:#ccc}

/* hero */
.hero{position:absolute;left:0;top:60px;width:1200px;height:372px;background:linear-gradient(180deg,#6f6f88 0%,#7c6f80 30%,#5c5a66 60%,#4a4a4f 100%)}
.hero h1{position:absolute;left:243px;top:135px;font-size:34px;font-weight:500;color:var(--white)}
.hero p{position:absolute;left:243px;top:178px;font-size:12px;font-weight:300;color:var(--white)}
.search-panel{position:absolute;left:245px;top:312px;width:710px;height:60px;background:rgba(255,255,255,.28)}
.select{position:absolute;top:18px;width:155px;height:27px;background:var(--white);border:1px solid #ddd;font-size:9px;padding:0 10px;display:flex;align-items:center;justify-content:space-between}

/* section headings */
.sec-title{position:absolute;font-size:18px;font-weight:300;color:#222}
.corner{position:absolute;width:36px;height:34px;border-left:2px solid var(--green);border-top:2px solid var(--green)}

/* about */
.about-list{position:absolute;left:270px;top:550px;width:305px;list-style:none;font-size:9px;line-height:15px;color:var(--muted);font-weight:300}
.about-list li{position:relative;padding-left:15px;margin-bottom:15px}
.about-list li::before{content:"";position:absolute;left:0;top:5px;width:5px;height:5px;background:var(--green)}

/* services */
.services{position:absolute;left:0;top:783px;width:1200px;height:318px;background:linear-gradient(90deg,#ededed,#f7f7f7 60%,#f2f2f2)}
.service-card{position:absolute;top:33px;width:212px;height:249px;background:var(--white)}
.service-card .head{position:absolute;left:10px;top:10px;width:192px;height:114px;background:var(--soft);display:flex;align-items:flex-end;justify-content:center;padding-bottom:14px;font-size:21px;font-weight:700;color:var(--green)}
.service-card h3{position:absolute;left:20px;top:144px;font-size:12px;font-weight:400}
.service-card p{position:absolute;left:20px;top:166px;width:180px;font-size:9px;line-height:15px;color:var(--muted);font-weight:300}

/* testimonial */
.quote-box{position:absolute;left:261px;top:1188px;width:680px;height:112px;border:1px solid var(--line)}
.quote-box p{position:absolute;left:104px;top:24px;width:560px;font-size:9px;line-height:19.5px;color:#555;font-weight:300}
.dots{position:absolute;right:26px;bottom:12px;display:flex;gap:6px}
.dots span{width:11px;height:2px;background:#ccc}
.dots .on{background:var(--green)}

/* works grid */
.tile{position:absolute;width:300px;height:230px;color:var(--white);font-size:12px;display:flex;align-items:flex-end;justify-content:center;padding-bottom:14px}

/* resources */
.post{position:absolute;top:1990px;width:317px;height:258px;background:var(--white);box-shadow:0 1px 4px rgba(0,0,0,.15)}
.post .photo{position:absolute;left:0;top:0;width:317px;height:152px}
.post .date{position:absolute;left:20px;top:130px;height:22px;padding:0 8px;background:var(--green);color:var(--white);font-size:9px;display:flex;align-items:center}
.post h3{position:absolute;left:20px;top:162px;width:280px;font-size:12px;font-weight:300;line-height:16px}
.post p{position:absolute;left:20px;width:280px;font-size:8.5px;line-height:15px;color:var(--muted);font-weight:300}
.post em{font-weight:700;color:var(--green-dark)}

/* newsletter */
.newsletter{position:absolute;left:0;top:2280px;width:1200px;height:68px;background:var(--green-band)}
.newsletter h2{position:absolute;left:265px;top:22px;font-size:18px;font-weight:300;color:var(--white)}
.email-field{position:absolute;left:489px;top:21px;width:354px;height:26px;background:var(--white);font-size:9px;color:#888;display:flex;align-items:center;padding-left:32px}
.subscribe{position:absolute;left:843px;top:21px;width:95px;height:26px;background:var(--green-dark);color:var(--white);font-size:9px;display:flex;align-items:center;justify-content:center}

/* footer */
.footer-links{position:absolute;left:588px;top:2383px;list-style:none;font-size:9px;line-height:19.5px;color:#444}
.footer-links li::before{content:"› ";color:#666}
.contact{position:absolute;left:774px;top:2384px;font-size:9px;line-height:14px;color:#444}
.contact h4{font-size:12px;font-weight:400;margin-bottom:9px;color:#222}
.copyright{position:absolute;left:0;top:2508px;width:1200px;text-align:center;font-size:9px;color:#555}
</style>
</head>
<body>

<header class="site-header">
  <div class="brand" style="left:246px;top:19px;font-size:16px"><span class="mark"></span>Brevand Finance</div>
  <nav class="main-nav">
    <span class="active">Home</span><span>About Us ˅</span><span>Loans ˅</span><span>Resources ˅</span><span>Contact Us ˅</span>
  </nav>
  <div class="social" style="left:750px;top:26px"><span></span><span></span><span></span></div>
  <div class="divider-v"></div>
  <span class="login">LOGIN</span>
  <div class="btn" style="left:862px;top:19px;width:95px;height:22px">⊘ APPLY NOW</div>
</header>

<section class="hero" role="img" aria-label="Two-storey suburban house with gabled roof at sunset">
  <h1>Sed Do Eiusmod Tempor</h1>
  <p>Exercitation ullamco laboris nisi ut aliquip ex ea commodo</p>
  <div class="btn" style="left:244px;top:208px;width:94px;height:24px">LEARN MORE <span class="chev">›</span></div>
  <div class="search-panel">
    <div class="select" style="left:13px">Area from <span>˅</span></div>
    <div class="select" style="left:188px">Property Status <span>˅</span></div>
    <div class="select" style="left:363px">Location <span>˅</span></div>
    <div class="btn" style="left:539px;top:18px;width:156px;height:27px;font-size:9px">SEARCH</div>
  </div>
</section>

<section class="about">
  <div class="corner" style="left:243px;top:466px;width:83px;height:86px"></div>
  <div class="abs" style="left:266px;top:491px;font-size:15px;font-weight:300">Local real estate experts</div>
  <div class="abs" style="left:266px;top:510px;font-size:19px;font-weight:300">lending to local real estate investors</div>
  <ul class="about-list">
    <li>Brevand Finance is a local business with local knowledge and strong industry relationships.A partner with a wide network who offers value added services.</li>
    <li>Brevand has an established pool of experienced investors available for your real estate investment needs</li>
    <li>Loans offered (Fix and Flip, Commercial)</li>
    <li>Why borrow from Brevand (experts, fast approval, professional, a partner, selective, competitive rates and fees)</li>
  </ul>
  <div class="abs" style="left:923px;top:713px;width:34px;height:34px;border-right:4px solid var(--green);border-bottom:4px solid var(--green)"></div>
  <div class="abs" role="img" aria-label="Bright white kitchen with window and flowers" style="left:611px;top:487px;width:341px;height:255px;background:linear-gradient(135deg,#e9e9ec,#cfd3d6 60%,#b9b3a8)"></div>
</section>

<section class="services">
  <div class="abs" role="img" aria-label="Line drawing of a building in perspective" style="left:0;top:0;width:490px;height:318px;background:linear-gradient(90deg,#e4e4e4,#ececec)"></div>
  <div class="service-card" style="left:250px">
    <div class="head">Buy a house</div>
    <h3>Buy a house</h3>
    <p>Sed ut perspiciatis unde omnis iste natus error sit voluptatem accusantium</p>
    <div class="btn" style="left:20px;top:209px;width:80px;height:20px">Learn More <span class="chev">›</span></div>
  </div>
  <div class="service-card" style="left:494px">
    <div class="head">Renovate</div>
    <h3>Renovate</h3>
    <p>Perspiciatis unde omnis iste natus error sit voluptatem accusantium doloremque</p>
    <div class="btn" style="left:20px;top:209px;width:80px;height:20px">Learn More <span class="chev">›</span></div>
  </div>
  <div class="service-card" style="left:738px">
    <div class="head">Sale</div>
    <h3>Sale</h3>
    <p>Spiciatis unde omnis iste natus error sit voluptatem accusantium doloremque</p>
    <div class="btn" style="left:20px;top:209px;width:80px;height:20px">Learn More <span class="chev">›</span></div>
  </div>
</section>

<section class="testimonials">
  <div class="corner" style="left:250px;top:1128px"></div>
  <h2 class="sec-title" style="left:265px;top:1144px">See What Our Clients Have to Say</h2>
  <div class="quote-box">
    <svg class="abs" style="left:20px;top:18px" width="68" height="78" viewBox="0 0 68 78" role="img" aria-label="Client portrait">
      <polygon points="34,0 68,19 68,59 34,78 0,59 0,19" fill="#c9c9c9"/>
      <polyline points="0,59 34,78 68,59" fill="none" stroke="#0d6332" stroke-width="4"/>
    </svg>
    <p>“I was in a time sensitive situation and my contact was able to give me better terms and rates than other lenders that I have had long time relationships with. I enjoy their streamlined online platform and am glad to have a financing partner that can move things along at the speed and efficiency that this business requires.”</p>
    <div class="abs" style="left:105px;top:88px;font-size:10px;color:#666">Doran K.</div>
    <div class="dots"><span></span><span class="on"></span><span></span></div>
  </div>
</section>

<div class="abs" style="left:0;top:1331px;width:1200px;height:1px;background:var(--line)"></div>

<section class="works">
  <div class="corner" style="left:250px;top:1357px"></div>
  <h2 class="sec-title" style="left:265px;top:1373px">See How It’s Worked For Others</h2>
  <div class="abs" style="left:265px;top:1402px;font-size:9px;color:#555;font-weight:300">Sed ut perspiciatis unde omnis iste natus error sit voluptatem accusantium doloremque laudantium</div>
  <div class="btn" style="left:856px;top:1397px;width:80px;height:20px">Learn More <span class="chev">›</span></div>

  <div class="tile" role="img" aria-label="Brick colonial house with trucks" style="left:0;top:1436px;background:linear-gradient(180deg,#b7bcc2,#8b7f76)">Perspiciatis</div>
  <div class="tile" role="img" aria-label="Single-storey house behind trees, green overlay" style="left:300px;top:1436px;background:#3f7a4b">
    <svg class="abs" style="left:135px;top:100px" width="29" height="29"><rect x=".5" y=".5" width="28" height="28" fill="none" stroke="#dfe" /><path d="M14.5 8v13M8 14.5h13" stroke="#fff"/></svg>
  </div>
  <div class="tile" role="img" aria-label="White house with porch and iron fence" style="left:600px;top:1436px;background:linear-gradient(180deg,#d7d9dc,#777)">Voluptatem</div>
  <div class="tile" role="img" aria-label="Red brick apartment building" style="left:900px;top:1436px;background:linear-gradient(180deg,#a3543f,#6e5548)">Accusantium</div>
  <div class="tile" role="img" aria-label="Ranch house with carport under trees" style="left:0;top:1666px;background:linear-gradient(180deg,#4d79b8,#4b5e3c)">doloremque</div>
  <div class="tile" role="img" aria-label="White sided bungalow with steps" style="left:300px;top:1666px;background:linear-gradient(180deg,#d9d9d9,#6f6f6f)">Laudantium</div>
  <div class="tile" role="img" aria-label="Brick two-storey house with shutters" style="left:600px;top:1666px;background:linear-gradient(180deg,#9a5444,#5d4a3a)">Aperiam</div>
  <div class="tile" role="img" aria-label="Beige cape cod house among trees" style="left:900px;top:1666px;background:linear-gradient(180deg,#6f8a58,#7c7462)">Inventore</div>
</section>

<section class="resources">
  <div class="corner" style="left:250px;top:1922px"></div>
  <h2 class="sec-title" style="left:265px;top:1938px">Investor Resources</h2>
  <div class="btn" style="left:856px;top:1936px;width:80px;height:20px">Learn More <span class="chev">›</span></div>

  <article class="post" style="left:266px">
    <div class="photo" role="img" aria-label="Bright home office with shelves and plant" style="background:linear-gradient(135deg,#f1efe9,#d9d2c4)"></div>
    <div class="date">13 SEPTEMBER 2017</div>
    <h3>The Advantages of Specialty Financing vs. Bank Financing for Rental Properties</h3>
    <p style="top:204px">What are the financing options for real estate investors looking to invest in rental properties? One option is to go the traditional bank route...<em>read more</em></p>
  </article>
  <article class="post" style="left:619px">
    <div class="photo" role="img" aria-label="Desk with laptop and floor plans, black and white" style="background:linear-gradient(135deg,#8d8d8d,#d1d1d1)"></div>
    <div class="date">20 SEPTEMBER 2017</div>
    <h3>Top Fix and Flip Markets in 2017</h3>
    <p style="top:186px">As the fix-and-flip industry continues to grow, real estate investors may be looking to expand their business into new markets.<br>One of the challenges investors face when...<em>read more</em></p>
  </article>
</section>

<section class="newsletter">
  <h2>Subscribe to Newsletter</h2>
  <div class="email-field">
    <svg class="abs" style="left:11px;top:8px" width="13" height="10"><rect x=".5" y=".5" width="12" height="9" fill="none" stroke="#999"/><path d="M.5 .5l6 5 6-5" fill="none" stroke="#999"/></svg>
    Type Your Email Address
  </div>
  <div class="subscribe">SUBSCRIBE</div>
</section>

<footer>
  <div class="brand" style="left:265px;top:2395px;font-size:15px"><span class="mark"></span>Brevand Finance</div>
  <p class="abs" style="left:265px;top:2442px;width:275px;font-size:9px;line-height:14px;color:#555">Lorem ipsum dolor sit amet, consectetur adipiscing elit, sed do eiusmod tempor incididunt ut labore et dolore magna aliqua. Ut enim ad minim veniam.</p>
  <ul class="footer-links">
    <li>Home</li><li>About Us</li><li>Loans</li><li>Resources</li><li>Contact Us</li>
  </ul>
  <div class="contact">
    <h4>Contact Us</h4>
    Brevand Finance<br>Phone:(123) 456-123<br>E-mail: lorempsum@example.com
  </div>
  <div class="social" style="left:774px;top:2467px"><span style="background:#ccc"></span><span style="background:#ccc"></span><span style="background:#ccc"></span></div>
  <div class="abs" style="left:0;top:2496px;width:1200px;height:1px;background:var(--line)"></div>
  <div class="copyright">Copyright 2017 Brevand Finance, All Rights Reserved</div>
</footer>

</body>
</html>
```